BrightVale business cards

We want to create two sets of cards. One general card for brightvale [staff] and one card for the founder of the company. Below is the general/basic information for you to format/display on side of the cards:
--Company address: 418 Marlow Street, New York, NY 10034
--Main phone: 212-563-7182
Will also provide you with secondary 1-800 number
--company website: www.brightvale-example.com
--email address for general card: concierge@brightvale-example.com
--email address (for dr lindqvist's card: dr@brightvale-example.com
--titles for dr lindqvist's card: Founder, Medical Director
--Dr. Lindqvist's name on the card should read: Martin E. Lindqvist, MD
You can also play around with brightvale's tag line: Glow Starts With Care (TM or R should be attached as a trademark has been filed)
Reason: More time to design something awesome. This company is an aesthetic medical company that offers cool and safe cosmetic treatments
For the business card design for the doctor, please change the doctor's name to look like this above his title: Martin E. Lindqvist, MD instead of using Dr. Martin....etc
Reason: WILL NOT BE ABLE TO VIEW AND FINALIZE DESIGNS UNTIL I RETURN FROM MEDICAL CONFERENCE, WHICH WILL BE ON SUNDAY/MONDAY. MY APOLOGIES
can everyone try making it very minimalistic
A Bit of a change...
Can everyone take a stab at using a grey "raw" or eco friendly stock paper. We are interested to see the designs you come up with.
Business

```html
<!DOCTYPE html>
<html lang="en">
<head>
<meta charset="utf-8">
<title>BrightVale Business Cards</title>
<link rel="stylesheet" href="https://fonts.googleapis.com/css2?family=Comfortaa:wght@400&family=Michroma&family=Nunito+Sans:wght@400;600&display=swap">
<style>
  :root {
    --backdrop: #707276;
    --stock: #d6d5d0;
    --stock-edge: #c9c8c2;
    --blue-deep: #2a72c9;
    --blue-light: #6fb2f0;
    --brand-blue: #2f7fd0;
    --tag-blue: #3b86cf;
    --name-red: #a82226;
    --ink: #2b2b2b;
    --white: #ffffff;
  }
  * { box-sizing: border-box; margin: 0; padding: 0; }
  html, body { width: 1200px; height: 895px; overflow: hidden; }
  body {
    background: var(--backdrop);
    display: flex;
    flex-direction: column;
    align-items: center;
    justify-content: center;
    gap: 36px;
    font-family: "Nunito Sans", sans-serif;
  }
  .card {
    position: relative;
    width: 700px;
    height: 400px;
    background: linear-gradient(135deg, var(--stock), var(--stock-edge));
    border-radius: 4px;
    box-shadow: 0 6px 18px rgba(0,0,0,0.3);
    overflow: hidden;
  }
  .accent-strip {
    position: absolute;
    right: 0;
    width: 160px;
    height: 28px;
    background: linear-gradient(90deg, var(--blue-light), var(--blue-deep));
  }
  .card-front .accent-strip { top: 0; }
  .card-back .accent-strip { top: 70px; }

  .brand {
    position: absolute;
    left: 0; right: 0; top: 150px;
    text-align: center;
  }
  .brand-name {
    font-family: "Comfortaa", sans-serif;
    font-weight: 400;
    font-size: 66px;
    letter-spacing: -1px;
    color: var(--brand-blue);
    line-height: 1;
  }
  .brand-tagline {
    margin-top: 8px;
    font-family: "Comfortaa", sans-serif;
    font-size: 10px;
    letter-spacing: 2.4px;
    color: var(--tag-blue);
    text-transform: uppercase;
  }
  .brand-tagline sup { font-size: 7px; letter-spacing: 0; }

  .person {
    position: absolute;
    right: 30px;
    top: 112px;
    text-align: left;
    font-family: "Michroma", sans-serif;
    text-transform: uppercase;
    white-space: nowrap;
  }
  .person-name { font-size: 21px; color: var(--ink); letter-spacing: 0.5px; }
  .person-name .first { color: var(--name-red); }
  .person-title { font-size: 13px; color: var(--ink); margin-top: 6px; letter-spacing: 1px; }

  .contact-panel {
    position: absolute;
    left: 22px;
    top: 196px;
    width: 560px;
    height: 184px;
    display: flex;
    gap: 3px;
  }
  .contact-cell {
    flex: 1;
    background: linear-gradient(160deg, var(--blue-light), var(--blue-deep));
    color: var(--white);
    display: flex;
    flex-direction: column;
    align-items: center;
    padding-top: 30px;
    font-size: 12px;
    line-height: 1.6;
    text-align: center;
    white-space: nowrap;
  }
  .contact-cell:first-child { border-radius: 12px 0 0 12px; }
  .contact-cell:last-child { border-radius: 0 12px 12px 0; }
  .contact-icon { width: 34px; height: 34px; margin-bottom: 22px; }
</style>
</head>
<body>
  <section class="card card-front">
    <div class="accent-strip"></div>
    <div class="brand">
      <div class="brand-name">brightvale</div>
      <div class="brand-tagline">Glow Starts With Care<sup>™</sup></div>
    </div>
  </section>

  <section class="card card-back">
    <div class="accent-strip"></div>
    <div class="person">
      <div class="person-name"><span class="first">Martin</span> E. Lindqvist, MD</div>
      <div class="person-title">Founder, Medical Director</div>
    </div>
    <div class="contact-panel">
      <div class="contact-cell">
        <svg class="contact-icon" viewBox="0 0 34 34" aria-hidden="true">
          <path d="M4 12c0-4 6-6 13-6s13 2 13 6v3h-7v-3c-2-1-10-1-12 0v3H4z" fill="#fff"/>
          <path d="M10 16h14l4 12H6z" fill="#fff"/>
          <circle cx="17" cy="22" r="3" fill="#3d8ad8"/>
        </svg>
        <span>212-563-7182</span>
        <span>1-800-555-0192</span>
      </div>
      <div class="contact-cell">
        <svg class="contact-icon" viewBox="0 0 34 34" aria-hidden="true">
          <g fill="none" stroke="#fff" stroke-width="2">
            <circle cx="17" cy="17" r="13"/>
            <ellipse cx="17" cy="17" rx="6" ry="13"/>
            <path d="M4 17h26M6 10h22M6 24h22"/>
          </g>
        </svg>
        <span>dr@brightvale-example.com</span>
        <span>www.brightvale-example.com</span>
      </div>
      <div class="contact-cell">
        <svg class="contact-icon" viewBox="0 0 34 34" aria-hidden="true">
          <path d="M17 3a10 10 0 0 0-10 10c0 8 10 18 10 18s10-10 10-18A10 10 0 0 0 17 3z" fill="#fff"/>
          <circle cx="17" cy="13" r="4" fill="#3d8ad8"/>
        </svg>
        <span>418 Marlow Street</span>
        <span>New York, NY 10034</span>
      </div>
    </div>
  </section>
</body>
</html>
```